Etiketten für hochwertigen bio Tee aus Österreich
Zielgruppe
Wir sind zwei Landwirte aus Österreich die hochwertigen Tee in Bioqualität produzieren. Dabei sind wir auf der Suche nach einem Klebeetikett für unsere Standbodenbeutel. Zielgruppe sind alle Teetrinker/innen die auf Lebensmittel und deren Herstellung hohen Wert legen und denen eine direkte Abnahme vom Landwirt ohne Zwischenhandel wichtig ist.
Aufgabenstellung
Es sollen erdige, bodenständige Farben verwendent werden. Bei der Produktion spielt die Kreislaufwirtschaft eine tragende Rolle. So wird Kompost für die Düngung am Feld selbst hergestellt. Darüber hinaus wird für das Trocknen der Teekräuter ein innovative Wärmerückgewinnung verwendent. Die Funktiontalität des Etikettes spielt auch eine wichtige Rolle - da es gleichzeitig als Versiegelung dient und beidseitig in umgedrehter Richtung bedruckt werden soll.
Es gibt unterschiedliche Teesorten die durch unterschiedliche Farben gekennzeichnet werden sollen: Apfelminze, Pfefferminze, Zitronenmelisse, Brennnessel aber auch Liebstock als Gewürz soll vermarktet werden. Im Bildanhang findent man eine bestehende Verpackung mit Logo (Vorder- und Rückseite) so wie es derzeit ist. Die Verpackung soll beibehalten werden und das Etikett soll daran angepasst werden. Die Dimension des Etikettes: Breite 7 cm Länge: 26 cm.
Ein Name (Morgenfeldhaus) und Logo sind bereits vorhanden. Der Name Morgenfeldhaus ist in Anlehnung an unsere Vierkantbauernhöfe zu sehen die meist quadratisch sind und sehr typisch für unsere Gegend.
Als Beispiel habe ich einen Wolkenbergetikett dazu gegeben. Grundsätzlich besteht es aus 2 Teilen: Dem Vorderteil und dem Hinterteil. Das Etikett wird über den Verschluß drüber geklebt - deshalb ist in der Mitte die Schrift um 180 Grad gedreht. Bei unserem Etikett soll nach 8 cm diese Drehung statt finden. Dieser Teil ist die Vorderansicht - er soll die Aufschrift der jeweiligen Teesorte also'BIO-Brennnesseltee' bzw. BIO-Apfelminztee usw. enthalten. sämtliche Teesorten enthalten. Darüber hinaus soll unser Morgenfeldhauslogo positioniert werden. Der Text 'für dich von uns am Hof verpackt' soll ebenfalls drauf stehen. Darüber hinaus der Text'höchste Qualität mit Liebe von Hand gemacht' soll ebanfalls auf der Vorderseite positioniert werden Am besten in einer möglichst handschriftlichen Schriftart. Auf der Rückseite des Etiketts so..

```html
<!DOCTYPE html>
<html lang="de">
<head>
<meta charset="utf-8">
<title>Morgenfeldhaus – Kräutertee Apfelminze Etikett</title>
<link rel="stylesheet" href="https://fonts.googleapis.com/css2?family=Caveat:wght@500;700&family=Roboto+Condensed:wght@300;400;700&display=swap">
<style>
  :root{
    --paper:#ebebe8;
    --paper-light:#f4f4f2;
    --green:#7bb52e;
    --green-dark:#5d8b26;
    --text-green:#6a8f2c;
    --ink:#3f3f3f;
    --white:#ffffff;
  }
  *{margin:0;padding:0;box-sizing:border-box}
  html,body{width:1200px;height:4196px;overflow:hidden;background:var(--paper)}
  body{font-family:"Roboto Condensed",sans-serif;color:var(--text-green)}
  .label{position:relative;width:1200px;height:4196px;overflow:hidden;
    background:linear-gradient(180deg,var(--paper-light) 0%,var(--paper) 40%,var(--paper-light) 100%)}
  .shapes{position:absolute;inset:0;width:1200px;height:4196px}
  .abs{position:absolute}

  .brand-name{left:66px;top:170px;font-size:88px;font-weight:400;color:var(--green-dark);letter-spacing:1px}
  .badge-text{left:95px;top:520px;font-family:"Caveat",cursive;font-weight:700;font-size:104px;line-height:.9;color:var(--white);transform:rotate(-6deg)}
  .handmade{left:100px;top:848px;font-family:"Caveat",cursive;font-weight:500;font-size:74px;color:var(--ink)}
  .weight{left:1022px;top:940px;font-size:58px;color:var(--white)}
  .variety-kicker{right:327px;top:1026px;font-size:54px;font-weight:300;color:var(--white);letter-spacing:1px}
  .variety-name{left:183px;top:1078px;font-size:124px;font-weight:700;color:var(--white);letter-spacing:7px;line-height:1}
  .tagline{left:66px;top:1236px;font-size:49px;font-weight:400;color:var(--text-green)}

  .story{left:62px;top:1426px;width:604px;height:1477px;background:rgba(255,255,255,.85);padding:14px 22px 0 24px;
    font-size:38px;font-weight:300;line-height:59px;color:var(--text-green);text-align:justify;hyphens:manual}
  .story p{margin-bottom:14px}
  .farm-sign{left:805px;top:2480px;font-size:54px;line-height:56px;color:#555;font-weight:300;transform:rotate(-3deg)}

  .ingredients{left:84px;top:3036px;width:560px;font-size:54px;font-weight:400;line-height:82px;color:var(--text-green)}
  .ingredients p{margin-bottom:14px;text-align:justify}
  .cert-code{left:90px;top:3852px;font-size:56px;color:var(--text-green)}
  .address{right:106px;top:3582px;text-align:right;font-size:57px;line-height:79px;color:var(--text-green)}
  .best-before{left:0;width:1200px;text-align:center;top:3952px;font-size:58px;line-height:84px;color:var(--text-green);word-spacing:6px}
</style>
</head>
<body>
<div class="label">
  <svg class="shapes" viewBox="0 0 715 2500" preserveAspectRatio="none">
    <defs>
      <radialGradient id="mint" cx="55%" cy="50%" r="55%">
        <stop offset="0" stop-color="#9fd24a"/>
        <stop offset="1" stop-color="#4f9a2a" stop-opacity=".9"/>
      </radialGradient>
      <linearGradient id="farm" x1="0" y1="0" x2="1" y2="1">
        <stop offset="0" stop-color="#cfcfcc"/>
        <stop offset=".6" stop-color="#b9b9b6"/>
        <stop offset="1" stop-color="#d8d8d5"/>
      </linearGradient>
      <linearGradient id="pot" x1="0" y1="0" x2="0" y2="1">
        <stop offset="0" stop-color="#e2e2df"/>
        <stop offset="1" stop-color="#cdd3c4"/>
      </linearGradient>
    </defs>
    <polygon points="0,88 88,0 425,0 508,128 268,398 0,146" fill="#ffffff" stroke="#5d8b26" stroke-width="4"/>
    <rect x="38" y="272" width="218" height="166" rx="10" fill="#7bb52e" transform="rotate(-4 147 355)"/>
    <g role="img" aria-label="Aquarell-Illustration eines Apfelminzzweigs">
      <ellipse cx="590" cy="345" rx="150" ry="290" fill="url(#mint)"/>
    </g>
    <rect x="30" y="603" width="572" height="122" fill="#7bb52e"/>
    <g role="img" aria-label="Graue Aquarellzeichnung eines Vierkanthofs">
      <rect x="0" y="780" width="715" height="970" fill="url(#farm)" opacity=".75"/>
    </g>
    <g role="img" aria-label="Zeichnung einer gepunkteten Teekanne mit zwei grünen Blättern">
      <rect x="410" y="1765" width="305" height="340" rx="60" fill="url(#pot)"/>
    </g>
    <rect x="50" y="2135" width="240" height="160" fill="#8cc63f"/>
  </svg>

  <div class="abs brand-name">Morgenfeldhaus</div>
  <div class="abs badge-text">100%<br>Bio</div>
  <div class="abs handmade">… mit Liebe von Hand gemacht</div>
  <div class="abs weight">50g</div>
  <div class="abs variety-kicker">KRÄUTERTEE</div>
  <div class="abs variety-name">APFELMINZE</div>
  <div class="abs tagline">Höchste Qualität - für Dich von uns am Hof verpackt!</div>

  <div class="abs story">
    <p>Mächtig und stolz erheben sich unsere Vierkanthöfe eingebettet in der Kulturlandschaft Oberöster&shy;reichs umringt von fruchtbaren Fel&shy;dern. Die Formgebung der meist quadratischen Vierkanthöfe ist aus&shy;schlaggebend für unseren Namen: Morgenfeldhaus.</p>
    <p>Neues Leben in alten Höfen<br>Auf unseren ursprünglichen Böden werden schon einige 100 Jahre und über Generationen hinweg un&shy;terschiedlichste Ackerfrüchte kul&shy;tiviert. Neu belebt werden unsere Felder durch vielfältige Kräuterar&shy;ten für unsere aromatischen Tees. Nachhaltigkeit im Umgang mit un&shy;serer Mutter Erde und den Pflanzen ist dabei oberstes Gebot und das schmeckt man auch im Tee.</p>
    <p>Nachhaltigkeit im Umgang mit un&shy;serer Mutter Erde und den Pflanzen ist dabei oberstes Gebot und das schmeckt man auch im Tee.</p>
  </div>
  <div class="abs farm-sign">Birkenhof<br>seit 1856</div>

  <div class="abs ingredients">
    <p>ZUTAT: Apfelminzblätter</p>
    <p>ZUBEREITUNG: 1 EL Tee pro Tasse mit kochen&shy;dem Wasser aufgießen, 5 - 10 Minuten ziehen lassen und abseihen.</p>
  </div>

  <div class="abs cert-code">AT-BIO-917</div>
  <div class="abs address">Familie Lindbauer<br>Birkenhof<br>4471 Wiesendorf<br>Auweg 7</div>

  <div class="abs best-before">Mindestens Haltbar bis: 01/01/22<br>Licht geschützt und trocken lagern</div>
</div>
</body>
</html>
```